Homemaking training schools needs a Business Card design

Designer, Hello!

No special requirements, good-looking enough.
--------------------------------------------------------------------------

Name: Marcus Liao
Chairman
Tel: 0574-57418263
Mobile: 13852247106
Email: kelvory@mailpond.com
Web: www.tqb2031.com
Add: No.258, LinfengJie, DaoyueQu, Ningbo, Zhejiang

LOGO
Ningbo TQB Homemaking Training School

Target Market(s)

pregnant women, mothers, infants, the elderly and families, including cleaning, cooking, nursing training.

Industry/Entity Type

Business

Contact Information for Business Card

Name: Marcus Liao
Chairman
Tel: 0574-57418263
Mobile: 13852247106
Email: kelvory@mailpond.com
Web: www.tqb2031.com

LOGO

Font styles to use
Serif
Sans Serif
Decorative

Requirements
Nice to have
• Feels: clean, specifications, safety, comfort, warmth and happiness.

```html
<!DOCTYPE html>
<html lang="en">
<head>
<meta charset="utf-8">
<title>TianQiBao Training &amp; Services – Business Card</title>
<link rel="stylesheet" href="https://fonts.googleapis.com/css2?family=Quicksand:wght@500;700&display=swap">
<style>
  :root {
    --stage: #2b2b2d;
    --card-white: #ffffff;
    --card-grey: #e9eaec;
    --brand-blue: #1f6fb4;
    --brand-pink: #e3157f;
    --ink: #333840;
    --light: #ffffff;
  }
  * { box-sizing: border-box; margin: 0; padding: 0; }
  html, body {
    width: 1200px; height: 997px; overflow: hidden;
    background: var(--stage);
    font-family: "Quicksand", sans-serif;
  }
  .stage {
    position: relative; width: 1200px; height: 997px;
    display: flex; align-items: center; justify-content: center; gap: 60px;
  }
  .card {
    position: relative; width: 520px; height: 300px; overflow: hidden;
    background: radial-gradient(ellipse at 40% 30%, var(--card-white) 55%, var(--card-grey) 100%);
    box-shadow: 0 10px 30px rgba(0,0,0,.45);
  }
  .card__band { position: absolute; inset: 0; width: 100%; height: 100%; }
  .card__band .band-fill { fill: var(--brand-blue); }
  .card__band .band-edge { fill: none; stroke: var(--brand-pink); stroke-width: 4; }

  .brand { position: absolute; text-align: center; color: var(--ink); font-weight: 500; }
  .brand__name { line-height: 1.1; }
  .brand__tagline { margin-top: 6px; }

  /* contact side */
  .card--contact .brand { left: 60px; top: 50px; width: 230px; }
  .card--contact .brand__name { font-size: 32px; }
  .card--contact .brand__tagline { font-size: 12px; }

  .contact-list {
    position: absolute; right: 18px; top: 120px; list-style: none;
    color: var(--light); font-size: 11.5px; font-weight: 500; text-align: right;
  }
  .contact-list li { display: flex; justify-content: flex-end; align-items: center; gap: 7px; margin-bottom: 5px; }
  .contact-list .icon {
    width: 12px; height: 12px; flex: none;
    background: var(--light); border-radius: 2px;
    display: flex; align-items: center; justify-content: center;
  }
  .contact-list .icon svg { width: 9px; height: 9px; fill: var(--brand-pink); }
  .contact-list .address { display: block; }

  .person { position: absolute; left: 26px; bottom: 26px; }
  .person__name { color: var(--light); font-size: 19px; font-weight: 500; line-height: 1.2; }
  .person__role { color: var(--brand-pink); font-size: 12px; font-weight: 500; margin-top: 2px; }

  /* front side */
  .card--front .brand { left: 0; right: 0; top: 64px; }
  .card--front .brand__name { font-size: 44px; }
  .card--front .brand__tagline { font-size: 15px; }

  .web {
    position: absolute; left: 0; right: 0; bottom: 38px; text-align: center;
    color: var(--light); font-size: 21px; font-weight: 500; letter-spacing: 2px;
  }
</style>
</head>
<body>
<main class="stage">

  <section class="card card--contact" aria-label="Business card, contact side">
    <svg class="card__band" viewBox="0 0 520 300" preserveAspectRatio="none" aria-hidden="true">
      <path class="band-fill" d="M0,215 Q330,190 520,20 L520,300 L0,300 Z"/>
      <path class="band-edge" d="M0,215 Q330,190 520,20"/>
    </svg>

    <div class="brand">
      <p class="brand__name">TianQiBao</p>
      <p class="brand__tagline">Training &amp; Services</p>
    </div>

    <ul class="contact-list">
      <li>0574-57418263<span class="icon"><svg viewBox="0 0 10 10"><path d="M2 0h2l1 3-1.5 1a6 6 0 0 0 2.5 2.5L7 5l3 1v2a2 2 0 0 1-2 2A8 8 0 0 1 0 2a2 2 0 0 1 2-2z"/></svg></span></li>
      <li>13852247106<span class="icon"><svg viewBox="0 0 10 10"><rect x="2.5" y="0" width="5" height="10" rx="1"/></svg></span></li>
      <li>kelvory@mailpond.com<span class="icon"><svg viewBox="0 0 10 10"><path d="M0 2h10v6H0z M0 2l5 3.5L10 2"/></svg></span></li>
      <li><span class="address">No.258, LinfengJie, DaoyueQu<br>Ningbo, Zhejiang</span><span class="icon"><svg viewBox="0 0 10 10"><path d="M5 0a3.5 3.5 0 0 1 3.5 3.5C8.5 6 5 10 5 10S1.5 6 1.5 3.5A3.5 3.5 0 0 1 5 0z"/></svg></span></li>
    </ul>

    <div class="person">
      <p class="person__name">Marcus Liao</p>
      <p class="person__role">Chairman</p>
    </div>
  </section>

  <section class="card card--front" aria-label="Business card, front side">
    <svg class="card__band" viewBox="0 0 520 300" preserveAspectRatio="none" aria-hidden="true">
      <path class="band-fill" d="M0,190 Q310,235 520,90 L520,300 L0,300 Z"/>
      <path class="band-edge" d="M0,190 Q310,235 520,90"/>
    </svg>

    <div class="brand">
      <p class="brand__name">TianQiBao</p>
      <p class="brand__tagline">Training &amp; Services</p>
    </div>

    <p class="web">www.tqb2031.com</p>
  </section>

</main>
</body>
</html>
```